Monthly Subscription Box Design for Books (Pinereads)

our url (site not up yet) is "www.pinereads-example.com" and a few of our logos are posted below to be used in the design of the box

our tagline is "A new shelf every month"

some guidance from our packaging partner
https://www.boxlumeprint-example.com/pages/building-your-artwork-in-illustrator
https://www.boxlumeprint-example.com/pages/art-guidelines
https://www.boxlumeprint-example.com/pages/ink-saturation
https://www.boxlumeprint-example.com/pages/do-not-rotate-artwork
https://www.boxlumeprint-example.com/pages/convert-text-to-outlines
https://www.boxlumeprint-example.com/pages/missing-dieline

Target Market(s)

parents/kids of kindergarten to 4th grade ... monthly subscription box of books

Industry/Entity Type

Book Publisher

Font styles to use
Serif
Sans Serif

Requirements
Must have
• A logo from the attached files and our url on the box; must use the CAD dieline attached and follow the design guidelines of boxlumeprint (attached)
Nice to have
• our tagline on the box design as well

```html
<!DOCTYPE html>
<html lang="en">
<head>
<meta charset="utf-8">
<title>Pinereads — Subscription Box Dieline</title>
<link rel="stylesheet" href="https://fonts.googleapis.com/css2?family=Montserrat:wght@400;500&display=swap">
<style>
  :root{
    --backdrop:#b5b5b5;
    --board:#ffffff;
    --teal:#3aab93;
    --slate:#666766;
    --ink:#5f6060;
    --cut:#f1b9b9;
    --fold:#e3e3e3;
  }
  *{margin:0;padding:0;box-sizing:border-box}
  html,body{width:1200px;height:960px;overflow:hidden;background:var(--backdrop)}
  .canvas{position:relative;width:1200px;height:960px;font-family:"Montserrat",sans-serif}
  .piece{position:absolute;background:var(--board)}
  .band{position:absolute;left:0;right:0}
  .band--teal{background:var(--teal)}
  .band--slate{background:var(--slate)}
  .fold-line{position:absolute;left:0;right:0;height:1px;background:var(--cut)}

  /* lid piece */
  .lid-side{left:53px;top:152px;width:72px;height:650px;border-radius:58px 0 0 58px;border-right:1px solid var(--fold)}
  .lid-side .fold-line{top:68px}
  .lid-side .fold-line.low{top:582px}
  .lid-flap-top{left:130px;top:156px;width:414px;height:76px;border-radius:22px 22px 0 0}
  .lid-flap-bottom{left:130px;top:724px;width:414px;height:74px;border-radius:0 0 22px 22px}
  .lid-face{left:124px;top:228px;width:430px;height:500px;border-bottom:1px solid var(--cut)}
  .lid-face .band--teal{top:0;height:210px}

  .brand-name{position:absolute;left:0;right:0;text-align:center;font-weight:500;color:var(--ink);line-height:1;letter-spacing:-.01em}
  .tagline{position:absolute;left:0;right:0;text-align:center;color:var(--ink);font-weight:400;line-height:1}
  .url{position:absolute;left:0;right:0;text-align:center;color:var(--ink);font-size:15px;line-height:1}
  .url .domain{color:var(--teal)}

  .lid-face .brand-name{top:300px;font-size:54px}
  .lid-face .tagline{top:366px;font-size:16px}
  .lid-face .url{top:452px}

  /* tray piece */
  .tray-side{top:222px;width:72px;height:508px;border-top:1px solid var(--cut);border-bottom:1px solid var(--cut)}
  .tray-side--left{left:556px}
  .tray-side--right{left:1057px;top:224px;height:508px}
  .tray-side .band--slate{top:0;height:216px;display:flex;align-items:center;justify-content:center}
  .vertical-url{writing-mode:vertical-rl;transform:rotate(180deg);color:#fff;font-size:12.5px}
  .side-name{position:absolute;left:0;right:0;bottom:36px;text-align:center;font-weight:500;font-size:12px;color:var(--ink)}

  .tray-tab{position:absolute;background:var(--board)}
  .tray-tab--tl{left:556px;top:60px;width:72px;height:162px;clip-path:polygon(0 0,58% 0,100% 28%,100% 100%,0 100%)}
  .tray-tab--bl{left:556px;top:734px;width:72px;height:160px;clip-path:polygon(0 0,100% 0,100% 72%,58% 100%,0 100%)}
  .tray-tab--tr{left:1057px;top:64px;width:71px;height:160px;clip-path:polygon(42% 0,100% 0,100% 100%,0 100%,0 28%)}
  .tray-tab--br{left:1057px;top:732px;width:71px;height:160px;clip-path:polygon(0 0,100% 0,100% 100%,42% 100%,0 72%)}

  .tray-flap-top{left:630px;top:64px;width:425px;height:82px;border-bottom:1px solid var(--fold)}
  .tray-flap-bottom{left:628px;top:738px;width:429px;height:76px;border-bottom:1px solid var(--fold)}
  .tray-flap-base{left:630px;top:816px;width:425px;height:74px}

  .tray-face{left:628px;top:146px;width:429px;height:592px;border-bottom:1px solid var(--cut)}
  .tray-face .band--slate{top:0;height:72px;display:flex;align-items:center;justify-content:center}
  .flipped-url{transform:rotate(180deg);color:#fff;font-size:15px}
  .tray-face .band--teal{top:72px;height:307px}
  .copy{position:absolute;left:26px;right:22px;top:114px;color:#fff;font-size:7.6px;line-height:11.5px;text-align:justify}
  .copy p+p{margin-top:11px}
  .tray-face .brand-name{top:436px;font-size:34px}
  .tray-face .tagline{top:480px;font-size:12px}
  .tray-face .url{top:540px}
</style>
</head>
<body>
<main class="canvas">

  <!-- lid -->
  <div class="piece lid-side"><span class="fold-line"></span><span class="fold-line low"></span></div>
  <div class="piece lid-flap-top"></div>
  <div class="piece lid-flap-bottom"></div>
  <section class="piece lid-face">
    <div class="band band--teal"></div>
    <h1 class="brand-name">pinereads</h1>
    <p class="tagline">A new shelf every month</p>
    <p class="url">www.<span class="domain">pinereads-example</span>.com</p>
  </section>

  <!-- tray -->
  <div class="tray-tab tray-tab--tl"></div>
  <div class="tray-tab tray-tab--bl"></div>
  <div class="tray-tab tray-tab--tr"></div>
  <div class="tray-tab tray-tab--br"></div>
  <div class="piece tray-flap-top"></div>
  <div class="piece tray-flap-bottom"></div>
  <div class="piece tray-flap-base"></div>

  <aside class="piece tray-side tray-side--left">
    <div class="band band--slate"><span class="vertical-url">www.pinereads-example.com</span></div>
    <p class="side-name">pinereads</p>
  </aside>

  <section class="piece tray-face">
    <div class="band band--slate"><span class="flipped-url">www.pinereads-example.com</span></div>
    <div class="band band--teal"></div>
    <div class="copy">
      <p>Lorem ipsum dolor sit amet, consectetuer adipiscing elit, sed diam nonummy nibh euismod tincidunt ut laoreet dolore magna aliquam erat volutpat. Ut wisi enim ad minim veniam, quis nostrud exerci tation ullamcorper suscipit lobortis nisl ut aliquip ex ea commodo consequat. Duis autem vel eum iriure dolor in hendrerit in vulputate velit esse molestie consequat, vel illum dolore eu feugiat nulla facilisis at vero eros et accumsan et iusto odio dignissim qui blandit praesent luptatum zzril delenit augue duis dolore te feugait nulla facilisi. Nam liber tempor cum soluta nobis eleifend option congue nihil imperdiet doming id quod mazim placerat facer possim assum.</p>
      <p>Typi non habent claritatem insitam; est usus legentis in iis qui facit eorum claritatem. Investigationes demonstraverunt lectores legere me lius quod ii legunt saepius. Claritas est etiam processus dynamicus, qui sequitur mutationem consuetudium lectorum. Mirum est notare quam littera gothica, quam nunc putamus parum claram, anteposuerit litterarum formas humanitatis per seacula quarta decima et quinta decima. Eodem modo typi, qui nunc nobis videntur parum clari, fiant sollemnes in futurum.</p>
    </div>
    <h2 class="brand-name">pinereads</h2>
    <p class="tagline">A new shelf every month</p>
    <p class="url">www.<span class="domain">pinereads-example</span>.com</p>
  </section>

  <aside class="piece tray-side tray-side--right">
    <div class="band band--slate"><span class="vertical-url">www.pinereads-example.com</span></div>
    <p class="side-name">pinereads</p>
  </aside>

</main>
</body>
</html>
```